Looking for updated Letterhead and Compliments Slips to go with our new updated logo. This stationary will be used for letters to suppliers and customers so needs to be practical while also quite classic.

We are an engineering company so needs to be clean and precise

Target Market(s)

SME'S and large automotive customers

Industry/Entity Type

Automotive

Font styles to use
Sans Serif

Colors
85acd3
0356a4
0792cd
33a6d7
85abd2
ffffff

Requirements
Must have
• Address details as below
• KT Fabrications Limited
• Hallmere Road
• Brackwell
• Thornshire
• LP47 9XZ, UK
• Telephone: +44 (0)1632 960418
• Fax: +44 (0)1632 960733
• Email: sales@ktfabrications.example
• Web: www.ktfabrications.example
Nice to have
• Nice to have some element of being a British Manufacturer

```html
<!DOCTYPE html>
<html lang="en">
<head>
<meta charset="utf-8">
<title>KT Fabrications – Stationery Set</title>
<link rel="stylesheet" href="https://fonts.googleapis.com/css2?family=Open+Sans:wght@400;600&display=swap">
<style>
  :root {
    --navy: #0356a4;
    --band: #1b4f8f;
    --sky: #85acd3;
    --cyan: #0792cd;
    --light-cyan: #33a6d7;
    --paper: #ffffff;
    --ink: #555a60;
    --backdrop: #e8e9eb;
    --edge: #d6d8db;
  }
  * { box-sizing: border-box; margin: 0; padding: 0; }
  html, body { width: 1200px; height: 1080px; overflow: hidden; }
  body {
    background: var(--backdrop);
    font-family: "Open Sans", Arial, sans-serif;
    color: var(--ink);
    position: relative;
  }

  .sheet {
    position: absolute;
    background: var(--paper);
    border: 1px solid var(--edge);
    overflow: hidden;
  }

  /* Brand name block */
  .brand {
    display: flex;
    align-items: center;
    gap: 7px;
    color: var(--navy);
    font-weight: 600;
    letter-spacing: 0.22em;
    white-space: nowrap;
  }
  .brand-dot {
    width: 10px; height: 10px;
    border-radius: 50%;
    background: var(--cyan);
    flex: none;
  }

  /* Contact lines with icons */
  .contact-list { list-style: none; text-align: right; }
  .contact-list li {
    display: flex;
    justify-content: flex-end;
    align-items: center;
    gap: 9px;
    white-space: nowrap;
  }
  .contact-list svg { width: 9px; height: 9px; flex: none; }

  /* Business card */
  .business-card { left: 63px; top: 83px; width: 395px; height: 228px; }
  .business-card .brand { position: absolute; right: 22px; top: 50px; font-size: 13px; }
  .business-card .company-name {
    position: absolute; left: 22px; top: 102px;
    font-size: 17px; color: var(--navy); font-weight: 400;
  }
  .business-card .card-band {
    position: absolute; left: 0; right: 0; top: 136px; bottom: 0;
    background: var(--band); color: var(--paper);
    font-size: 11px; line-height: 12.6px;
  }
  .card-band address { position: absolute; left: 22px; top: 16px; font-style: normal; }
  .card-band .contact-list { position: absolute; right: 22px; top: 16px; }
  .card-band .contact-list svg { fill: var(--sky); }

  /* Letterhead */
  .letterhead { left: 507px; top: 83px; width: 625px; height: 882px; }
  .letterhead .brand { position: absolute; left: 78px; top: 64px; font-size: 14px; }
  .letterhead .contact-list {
    position: absolute; right: 52px; top: 38px;
    font-size: 11px; line-height: 13px;
  }
  .letterhead .contact-list svg { fill: var(--light-cyan); }
  .letterhead .head-rule {
    position: absolute; left: 78px; right: 52px; top: 114px;
    height: 2px; background: var(--sky);
  }
  .letter-body {
    position: absolute; left: 78px; right: 52px; top: 163px;
    font-size: 11.5px; line-height: 21px;
  }
  .letter-body .recipient { margin-bottom: 21px; }
  .letter-body .paragraph {
    text-align: justify; line-height: 19px; margin-bottom: 19px;
  }
  .letterhead .sender-address {
    position: absolute; right: 52px; top: 762px;
    text-align: right; font-style: normal; font-size: 11px; line-height: 13px;
  }
  .letterhead .foot-band {
    position: absolute; left: 0; right: 0; bottom: 0; height: 21px;
    background: var(--band);
  }

  /* DL envelope */
  .envelope { left: 40px; top: 560px; width: 440px; height: 220px; }
  .envelope .brand { position: absolute; left: 24px; top: 50px; font-size: 13px; }
  .envelope .address-window {
    position: absolute; left: 22px; top: 110px; width: 170px; height: 68px;
    border: 2px solid #cfd1d4; border-radius: 10px;
  }
  .envelope .contact-list {
    position: absolute; right: 16px; top: 116px;
    font-size: 10.5px; line-height: 13px;
  }
  .envelope .contact-list svg { fill: var(--light-cyan); }
  .envelope .foot-band {
    position: absolute; left: 0; right: 0; bottom: 0; height: 16px;
    background: var(--band);
  }
</style>
</head>
<body>

<svg width="0" height="0" style="position:absolute" aria-hidden="true">
  <symbol id="icon-phone" viewBox="0 0 10 10"><rect x="1" y="1" width="8" height="8" rx="1.5"/></symbol>
  <symbol id="icon-fax" viewBox="0 0 10 10"><path d="M5 1 L9 9 L1 9 Z"/></symbol>
  <symbol id="icon-web" viewBox="0 0 10 10"><circle cx="5" cy="5" r="4"/></symbol>
  <symbol id="icon-mail" viewBox="0 0 10 10"><rect x="0.5" y="2" width="9" height="6"/></symbol>
</svg>

<!-- Business card -->
<section class="sheet business-card">
  <div class="brand"><span class="brand-dot"></span>KT FABRICATIONS</div>
  <h1 class="company-name">KT Fabrications Limited</h1>
  <div class="card-band">
    <address>Hallmere Road<br>Brackwell<br>Thornshire<br>LP47 9XZ, UK</address>
    <ul class="contact-list">
      <li>+44 (0)1632 960418 <svg><use href="#icon-phone"/></svg></li>
      <li>+44 (0)1632 960733 <svg><use href="#icon-fax"/></svg></li>
      <li>www.ktfabrications.example <svg><use href="#icon-web"/></svg></li>
      <li>sales@ktfabrications.example <svg><use href="#icon-mail"/></svg></li>
    </ul>
  </div>
</section>

<!-- Letterhead -->
<section class="sheet letterhead">
  <div class="brand"><span class="brand-dot"></span>KT FABRICATIONS</div>
  <ul class="contact-list">
    <li>+44 (0)1632 960418 <svg><use href="#icon-phone"/></svg></li>
    <li>+44 (0)1632 960733 <svg><use href="#icon-fax"/></svg></li>
    <li>www.ktfabrications.example <svg><use href="#icon-web"/></svg></li>
    <li>sales@ktfabrications.example <svg><use href="#icon-mail"/></svg></li>
  </ul>
  <div class="head-rule"></div>

  <div class="letter-body">
    <p class="recipient">Mara Quill<br>Title<br>Company Name<br>4321 First Street<br>Anytown, State ZIP<br>Date 1/30/12</p>
    <p>Dear Mara,</p>
    <p class="paragraph">Lorem ipsum dolor sit amet, consectetur adipiscing elit, set eiusmod tempor incidunt et labore et dolore magna aliquam. Ut enim ad minim veniam, quis nostrud exerc. Irure dolor in reprehend incididunt ut labore et dolore magna aliqua. Ut enim ad minim is nostrud exercitation ullam mmodo consequet. Duis aute irure dolor in reprehenderit in voluptate velit esse cillum dolore eu fugiat nulla pariatur. At vver eos et accusam dignissum qui blandit est praesent. Mara quill beynoc lorem sed nisi ut aliquip ex ea commodo consequat, vel illum dolore eu feugiat nulla facilisis. Offectivo immoriatoly, nam liber tempor cum soluta nobis eleifend option congue nihil imperdiet doming id quod mazim placerat facer possim assum, quod erat demonstrandum.</p>
    <p class="paragraph">Nam liber tempor cum soluta nobis eleifend option congue nihil imperdiet doming id quod mazim placerat. Typi non habent claritatem insitam; est usus legentis in iis qui facit eorum claritatem mixent phona, investigationes demonstraverunt lectores.</p>
  </div>

  <address class="sender-address">Hallmere Road<br>Brackwell<br>Thornshire<br>LP47 9XZ, UK</address>
  <div class="foot-band"></div>
</section>

<!-- Envelope -->
<section class="sheet envelope">
  <div class="brand"><span class="brand-dot"></span>KT FABRICATIONS</div>
  <div class="address-window"></div>
  <ul class="contact-list">
    <li>+44 (0)1632 960418 <svg><use href="#icon-phone"/></svg></li>
    <li>+44 (0)1632 960733 <svg><use href="#icon-fax"/></svg></li>
    <li>www.ktfabrications.example <svg><use href="#icon-web"/></svg></li>
    <li>sales@ktfabrications.example <svg><use href="#icon-mail"/></svg></li>
  </ul>
  <div class="foot-band"></div>
</section>

</body>
</html>
```